Ferrowave.com website design

I need a basic website for www.ferrowave.com. Ferro Wave has been hosting websites since 2002 via partnership arrangement with Stackhollow.com and Namequarry.com. We do not do any design, only hosting for small companies and nonprofits. We are referring people to PixelGuild and others to get their websites developed. Our website and pricing does not change often, but I need to be able to easily update the pricing and contact page.

Target Market(s)

Small company and non profit organizations

Industry/Entity Type

Utility

Coding

Coded - Design and coding required

Number of Pages Required

5+ page

Colors

Designer to choose colors to be used in the design.

Requirements
Must have
• Wordsmith format for easy content management. The logo attached. Contact us page with the following: Phone and fax are the same number: 888.514.2973. Email address is myferrowave@mailnest.example. Mailing address is 4819 E. Tolliver Bend #317, Searcy, AR 72143.
Nice to have
• Some kind of badge or tag line on the home page that celebrates our 15th year of hosting without a single hosting without any downtime. We are are 15 year partners with Stackhollow.com and Namequarry.com. Website Design tab needs to reference PixelGuild or others for all their website design needs. We provide no design or updating services. We will provide the developers FTP access to our dedicated Linux server. We do not provide email services other than redirects to their proprietary email or gmail, yahoo, etc. Needs a services and pricing tab. We provide domain registration services via our partnership with Namequarry.com. We will want a way for them to submit a suggested domain name for us to verify if available. I might be able to get a link from Namequarry.com to our account for you to include on that tab REGISTER DOMAIN. The tab buttons can be: WHO WE ARE, WHAT WE DO, WHEN YOU NEED US, WHERE TO REACH US. Maybe consider making the WHO, WHAT, WHEN and WHERE a dark blue color the rest of the text different color just so they stand out
Should not have
• A lot of animation that takes a long time to open. Clean and simple website.

```html
<!DOCTYPE html>
<html lang="en">
<head>
<meta charset="utf-8">
<title>Ferro Wave – Hosting</title>
<link href="https://fonts.googleapis.com/css2?family=Lato:wght@300;400;700;900&display=swap" rel="stylesheet">
<style>
  :root{
    --navy:#0e2743;
    --navy-deep:#0a1e35;
    --blue:#2a8dd8;
    --blue-footer:#3b8fd1;
    --text:#555b63;
    --muted:#8d939a;
    --rule:#e3e6ea;
    --white:#ffffff;
    --label:rgba(14,39,67,.7);
  }
  *{box-sizing:border-box;margin:0;padding:0}
  html,body{width:750px;height:1200px;overflow:hidden}
  body{font-family:'Lato',Arial,sans-serif;color:var(--text);background:var(--white);position:relative}

  .topbar{height:15px;background:var(--navy-deep);display:flex;justify-content:space-between;align-items:center;padding:0 100px;font-size:7px;color:#c9d3de;letter-spacing:.5px}
  .topbar .search{display:flex;align-items:center;gap:6px;background:#1b3554;height:10px;width:150px;padding:0 5px;justify-content:space-between}

  .brand{height:100px;display:flex;flex-direction:column;align-items:center;justify-content:center;gap:4px}
  .brand-mark{width:34px;height:34px;background:var(--blue)}
  .brand-name{font-size:22px;font-weight:900;color:var(--navy);letter-spacing:1px;text-transform:uppercase}
  .brand-tag{font-size:7px;color:var(--muted);letter-spacing:2px}

  .mainnav{height:30px;display:flex;justify-content:center;gap:26px;align-items:center;font-size:9px;font-weight:700;color:var(--blue);letter-spacing:.5px}
  .mainnav b{color:var(--navy);font-weight:900}

  .hero{position:relative;height:217px;background:linear-gradient(120deg,#c9ced4 0%,#eef0f2 40%,#b8bfc8 70%,#6d7682 100%)}
  .hero-photo{position:absolute;inset:0;background:linear-gradient(90deg,rgba(14,39,67,.35),rgba(14,39,67,.15) 50%,rgba(14,39,67,.4))}
  .badge{position:absolute;left:50%;top:18px;transform:translateX(-50%);width:190px;height:180px}
  .badge svg{position:absolute;inset:0}
  .badge-text{position:absolute;inset:0;display:flex;flex-direction:column;align-items:center;justify-content:center;color:var(--white);text-align:center}
  .badge-kicker{font-size:7px;letter-spacing:2px;margin-bottom:8px;background:var(--label);padding:4px 10px;line-height:1}
  .badge-title{font-size:26px;font-weight:300;white-space:nowrap;letter-spacing:.5px;line-height:1}
  .badge-title strong{font-weight:900}
  .badge-foot{font-size:7px;letter-spacing:2px;margin-top:8px;background:var(--label);padding:4px 10px;line-height:1.35}

  .domain-bar{height:43px;background:var(--navy);display:flex;align-items:center;padding:0 100px 0 155px;gap:60px}
  .domain-bar h3{font-size:11px;color:var(--white);font-weight:900;letter-spacing:.5px}
  .domain-bar h3 span{color:var(--blue)}
  .domain-bar p{font-size:7px;color:#9fb0c3;margin-top:2px}
  .domain-form{display:flex;gap:8px;margin-left:auto}
  .domain-input{width:170px;height:16px;background:var(--white);font-size:7px;color:var(--muted);padding:4px 6px}
  .btn-blue{height:16px;padding:0 18px;background:var(--blue);color:var(--white);font-size:7px;font-weight:700;display:flex;align-items:center}

  .section-title{font-size:22px;font-weight:900;color:var(--navy);text-align:center;letter-spacing:.5px}
  .section-title span{color:var(--blue)}

  .services{padding-top:40px}
  .service-list{margin-top:20px}
  .service{display:flex;gap:32px;padding:0 100px 0 160px;height:92px}
  .service-icon{width:52px;height:52px;border-radius:50%;background:#f0f2f5;display:flex;align-items:center;justify-content:center;flex:none}
  .service h4{font-size:17px;font-weight:400;color:var(--blue);letter-spacing:.5px}
  .service h4 .price{color:var(--navy);font-weight:700;margin-left:16px;font-size:14px}
  .service p{font-size:7.5px;line-height:1.5;color:var(--muted);margin-top:5px}
  .read-more{font-size:6.5px;color:var(--blue);font-weight:700;margin-top:5px}

  .rule{height:1px;background:var(--rule);margin:0 100px}

  .split{display:flex;gap:40px;padding:28px 100px 0 110px;height:228px}
  .about{flex:1}
  .about h2,.partners h2{font-size:19px;font-weight:900;color:var(--navy)}
  .about h2 span,.partners h2 span{color:var(--blue)}
  .about p{font-size:7.5px;line-height:1.6;color:var(--muted);margin-top:14px}
  .btn-navy{display:inline-block;margin-top:14px;background:var(--navy);color:var(--white);font-size:7px;font-weight:700;padding:6px 12px}
  .partners{width:290px}
  .partner-panel{position:relative;margin-top:16px;height:126px;background:linear-gradient(135deg,#b9a58a,#e8ddcc 45%,#7b8a98)}
  .partner-badge{position:absolute;left:84px;width:96px;height:26px;background:var(--white)}
  .partner-badge.dark{background:#2a2d31}

  .contact{position:absolute;top:980px;left:0;width:750px;height:158px;background:var(--navy);color:var(--white);text-align:center}
  .contact h2{font-size:17px;font-weight:900;padding-top:32px}
  .contact h2 span{color:var(--blue)}
  .contact-cols{display:flex;justify-content:center;gap:70px;margin-top:18px}
  .contact-col h5{font-size:10px;font-weight:400;letter-spacing:1px}
  .contact-col p{font-size:7px;color:#a9b8c8;margin-top:4px;line-height:1.4}
  .social{display:flex;justify-content:center;gap:10px;margin-top:10px}
  .social i{width:9px;height:9px;border-radius:50%;background:var(--white);display:block}

  .site-footer{position:absolute;top:1138px;left:0;width:750px;height:62px;background:var(--blue-footer);color:var(--white);text-align:center;font-size:7px;padding-top:20px}
  .site-footer p+p{margin-top:6px;color:#dceaf6}
</style>
</head>
<body>

<header>
  <div class="topbar">
    <span>HOME &nbsp;|&nbsp; REGISTER</span>
    <span class="search">SEARCH
      <svg width="6" height="6" viewBox="0 0 10 10"><circle cx="4" cy="4" r="3" fill="none" stroke="#c9d3de" stroke-width="1.5"/><line x1="6.5" y1="6.5" x2="9.5" y2="9.5" stroke="#c9d3de" stroke-width="1.5"/></svg>
    </span>
  </div>
  <div class="brand">
    <div class="brand-mark"></div>
    <div class="brand-name">Ferro Wave</div>
    <div class="brand-tag">HOSTING · DOMAINS</div>
  </div>
  <nav class="mainnav">
    <span><b>WHO</b> WE ARE</span>
    <span><b>WHAT</b> WE DO</span>
    <span><b>WHEN</b> YOU NEED US</span>
    <span><b>WHERE</b> TO REACH US</span>
  </nav>
</header>

<section class="hero">
  <div class="hero-photo" role="img" aria-label="Photo of a laptop on a desk showing business charts"></div>
  <div class="badge">
    <svg width="190" height="180" viewBox="0 0 190 180">
      <polygon points="95,4 182,48 182,132 95,176 8,132 8,48" fill="none" stroke="#ffffff" stroke-width="2"/>
    </svg>
    <div class="badge-text">
      <div class="badge-kicker">CELEBRATING</div>
      <div class="badge-title"><strong>15 YEARS</strong> OF HOSTING</div>
      <div class="badge-foot">WITHOUT ANY<br>DOWNTIME</div>
    </div>
  </div>
</section>

<section class="domain-bar">
  <div>
    <h3>SUGGEST A <span>DOMAIN NAME</span></h3>
    <p>Verify a suggested domain name's availability</p>
  </div>
  <div class="domain-form">
    <div class="domain-input">Enter your domain name</div>
    <div class="btn-blue">SUBMIT</div>
  </div>
</section>

<section class="services">
  <h2 class="section-title">OUR <span>SERVICES</span></h2>
  <div class="service-list">
    <article class="service">
      <div class="service-icon">
        <svg width="26" height="22" viewBox="0 0 26 22"><path d="M6 14a5 5 0 0 1 1-9.8A7 7 0 0 1 20 6a4 4 0 0 1 0 8z" fill="none" stroke="#0e2743" stroke-width="1.5"/><line x1="13" y1="14" x2="13" y2="20" stroke="#0e2743" stroke-width="1.5"/><line x1="7" y1="20" x2="19" y2="20" stroke="#0e2743" stroke-width="1.5"/></svg>
      </div>
      <div>
        <h4>WEB HOSTING <span class="price">$9.99</span></h4>
        <p>Reliable Linux hosting for small companies and nonprofits on our dedicated server, with developer FTP access, daily backups and fifteen years of uptime without a single outage.</p>
        <div class="read-more">READ MORE »</div>
      </div>
    </article>
    <article class="service">
      <div class="service-icon">
        <svg width="24" height="22" viewBox="0 0 24 22"><rect x="2" y="2" width="20" height="14" fill="none" stroke="#0e2743" stroke-width="1.5"/><line x1="12" y1="16" x2="12" y2="20" stroke="#0e2743" stroke-width="1.5"/><line x1="6" y1="20" x2="18" y2="20" stroke="#0e2743" stroke-width="1.5"/><line x1="6" y1="9" x2="18" y2="9" stroke="#2a8dd8" stroke-width="1.5"/></svg>
      </div>
      <div>
        <h4>DOMAIN REGISTRATION <span class="price">$9.99</span></h4>
        <p>Find and register the right name for your organization through our long standing partnership with Namequarry.com. Send us a suggestion and we will verify it is available for you.</p>
        <div class="read-more">READ MORE »</div>
      </div>
    </article>
    <article class="service">
      <div class="service-icon">
        <svg width="22" height="22" viewBox="0 0 22 22"><rect x="2" y="9" width="4" height="11" fill="none" stroke="#0e2743" stroke-width="1.5"/><path d="M6 10l4-8c2 0 3 1 2.5 3L12 9h6a2 2 0 0 1 2 2.4l-1.5 7A2 2 0 0 1 16.6 20H6" fill="none" stroke="#0e2743" stroke-width="1.5"/></svg>
      </div>
      <div>
        <h4>WEB DEVELOPMENT SOLUTION <span class="price">$9.99</span></h4>
        <p>We do not design sites ourselves. We refer you to PixelGuild and other trusted developers, then give them FTP access to host your finished website with us.</p>
        <div class="read-more">READ MORE »</div>
      </div>
    </article>
  </div>
</section>

<div class="rule"></div>

<section class="split">
  <div class="about">
    <h2>ABOUT <span>FERRO WAVE</span></h2>
    <p>Ferro Wave has been hosting websites for small companies and nonprofit organizations since 2002. Through partnerships with Stackhollow.com and Namequarry.com we keep your site online, your domain secure and your pricing simple, so you can focus on your mission.</p>
    <span class="btn-navy">READ MORE</span>
  </div>
  <div class="partners">
    <h2>OUR <span>PARTNERS</span></h2>
    <div class="partner-panel" role="img" aria-label="Photo of a bright office workspace behind the partner badges">
      <div class="partner-badge" style="top:38px"></div>
      <div class="partner-badge dark" style="top:70px"></div>
    </div>
  </div>
</section>

<section class="contact">
  <h2>CONTACT <span>DETAILS</span></h2>
  <div class="contact-cols">
    <div class="contact-col"><h5>PHONE &amp; FAX NO.</h5><p>888.514.2973</p></div>
    <div class="contact-col"><h5>EMAIL ADDRESS</h5><p>myferrowave@mailnest.example</p></div>
    <div class="contact-col"><h5>ADDRESS</h5><p>4819 E. Tolliver Bend #317,<br>Searcy, AR 72143</p></div>
  </div>
  <div class="social"><i></i><i></i><i></i></div>
</section>

<footer class="site-footer">
  <p>Home · Who We Are · What We Do · When You Need Us · Where To Reach Us</p>
  <p>© 2017 Ferro Wave. All Rights Reserved.</p>
</footer>

</body>
</html>
```